New Chiropractic Office needs a fresh flyer design!

We need a flyer design for our chiropractic office for our hometown based chiropractic office called "Corvale Chiropractic" Dr. Martin Corvale provides chiropractic services including adjustments, xrays and wellness exercises with a fresh approach to chiropractic which focuses on getting your body aligned correctly to be a better you. We dont like to focus on coming in just for pain although that is what most people associate our operation with so we understand that comes with the territory. However we would like our flyers to express health and wellness rather than medical or pain. We would like our flyer to emphasize our "New Patient Special" which includes consultation, exam, xrays and first treatment for only $50. We also accept most insurance plans. Call for an appointment 618-390-2757.

Industry/Entity Type

Office

```html
<!DOCTYPE html>
<html lang="en">
<head>
<meta charset="utf-8">
<title>Corvale Chiropractic – New Patient Special</title>
<link rel="stylesheet" href="https://fonts.googleapis.com/css2?family=Open+Sans:wght@400;600;700&family=Oswald:wght@500;600&family=Dancing+Script:wght@400&family=Libre+Baskerville:wght@400&display=swap">
<style>
  :root {
    --green: #8cc63f;
    --green-dark: #6fa52a;
    --grey: #5f6062;
    --grey-dark: #4a4b4d;
    --ink: #2b2b2b;
    --paper: #ffffff;
    --paper-soft: #f4f4f2;
  }
  * { margin: 0; padding: 0; box-sizing: border-box; }
  html, body { width: 904px; height: 1200px; overflow: hidden; background: var(--paper); }
  .flyer {
    position: relative; width: 904px; height: 1200px; overflow: hidden;
    background: linear-gradient(180deg, var(--paper) 0%, var(--paper-soft) 100%);
    font-family: "Open Sans", Arial, sans-serif; color: var(--ink);
  }
  .website {
    position: absolute; left: 12px; top: 42px;
    font-family: "Libre Baskerville", Georgia, serif; font-size: 27px; color: var(--green-dark);
  }
  .brand {
    position: absolute; right: 34px; top: 36px;
    display: flex; flex-direction: column; align-items: center; gap: 12px;
  }
  .brand-dot { width: 56px; height: 56px; border-radius: 50%; background: var(--grey); }
  .brand-name {
    font-family: "Open Sans", Arial, sans-serif; font-weight: 600; font-size: 24px;
    color: var(--grey-dark); text-transform: uppercase; letter-spacing: 0.5px; white-space: nowrap;
  }
  .hero-art { position: absolute; left: 0; top: 0; }
  .hero-title {
    position: absolute; left: 22px; top: 472px;
    font-size: 29px; font-weight: 700; line-height: 1.18; color: var(--paper);
    text-shadow: 0 2px 4px rgba(0,0,0,.45);
  }
  .mission { position: absolute; left: 18px; top: 706px; width: 420px; }
  .mission-script {
    font-family: "Dancing Script", cursive; font-size: 40px; line-height: 1.25; color: var(--grey-dark);
  }
  .mission-text { margin-top: 18px; font-size: 16.5px; line-height: 1.3; font-weight: 600; color: var(--ink); }
  .mission-text .hl { color: var(--green-dark); font-weight: 700; text-transform: uppercase; }
  .services {
    position: absolute; left: 615px; top: 660px; width: 258px; height: 236px;
    background: var(--grey); color: var(--paper); padding: 14px 14px;
    box-shadow: 0 4px 8px rgba(0,0,0,.3); border-radius: 0 0 6px 6px;
  }
  .services-title { font-size: 24px; color: var(--green); font-weight: 400; margin-bottom: 28px; letter-spacing: .5px; }
  .services-list { list-style: none; font-size: 21px; line-height: 1.38; }
  .services-list li::before { content: "\203A"; color: var(--green); font-weight: 700; margin-right: 6px; }
  .services-list .note { font-size: 16px; line-height: 1.3; padding-left: 16px; }
  .services-list .note::before { content: none; }
  .offer-strip { position: absolute; left: 0; top: 943px; width: 904px; height: 24px; background: var(--grey-dark); }
  .offer-band {
    position: absolute; left: 0; top: 967px; width: 904px; height: 90px; background: var(--green);
    box-shadow: 0 3px 6px rgba(0,0,0,.25);
  }
  .offer-includes {
    position: absolute; left: 24px; top: 976px; width: 330px;
    color: var(--paper); font-size: 26px; font-weight: 600; line-height: 1.4;
  }
  .offer-includes span { margin-right: 18px; white-space: nowrap; }
  .offer-includes span::before { content: "\2713"; font-size: 18px; margin-right: 3px; }
  .offer-price {
    position: absolute; right: 22px; top: 974px; text-align: center;
    font-family: "Oswald", "Arial Narrow", sans-serif; font-weight: 600; line-height: 1.05;
  }
  .offer-price .lead { font-size: 37px; color: var(--ink); }
  .offer-price .amount { font-size: 40px; color: var(--paper); }
  .badge { position: absolute; left: 329px; top: 829px; }
  .badge-text {
    position: absolute; left: 329px; top: 875px; width: 250px; text-align: center;
    font-family: "Oswald", "Arial Narrow", sans-serif; font-weight: 600; font-size: 40px; line-height: 1.18;
    color: var(--paper);
  }
  .insurance {
    position: absolute; left: 0; top: 1092px; width: 904px; text-align: center;
    font-size: 25px; font-weight: 600; color: var(--green-dark); letter-spacing: .3px;
  }
  .call {
    position: absolute; left: 112px; top: 1140px; width: 683px; height: 56px;
    background: var(--grey); border-radius: 10px 10px 0 0;
    display: flex; align-items: center; justify-content: center; gap: 14px;
    color: var(--paper); font-size: 28px;
  }
  .call-number { color: var(--green); font-weight: 600; font-size: 31px; display: flex; align-items: center; gap: 6px; }
  .footer-strip { position: absolute; left: 0; top: 1194px; width: 904px; height: 6px; background: var(--grey); }
</style>
</head>
<body>
<main class="flyer">
  <div class="website">www.corvalechiropractic.com</div>

  <div class="brand">
    <div class="brand-dot"></div>
    <div class="brand-name">Corvale Chiropractic</div>
  </div>

  <svg class="hero-art" width="904" height="780" viewBox="0 0 904 780">
    <defs>
      <linearGradient id="heroTone" x1="0" y1="0" x2="1" y2="1">
        <stop offset="0" stop-color="#7f9b5a"/>
        <stop offset="0.45" stop-color="#c9d3bd"/>
        <stop offset="0.75" stop-color="#5a88b8"/>
        <stop offset="1" stop-color="#b9c1b0"/>
      </linearGradient>
    </defs>
    <g role="img" aria-label="Photo: smiling older couple outdoors, the woman riding piggyback on the man, green trees behind">
      <path d="M0,160 Q430,178 904,322 L904,690 Q470,640 0,610 Z" fill="url(#heroTone)"/>
    </g>
    <path d="M0,152 Q430,170 904,312" fill="none" stroke="#5f6062" stroke-width="6"/>
    <path d="M230,168 Q600,200 904,300 L904,336 Q620,222 230,168 Z" fill="#8cc63f"/>
    <path d="M0,610 Q470,640 904,690" fill="none" stroke="#5f6062" stroke-width="7"/>
    <path d="M0,622 Q470,652 904,702 L904,716 Q470,666 0,640 Z" fill="#8cc63f"/>
  </svg>

  <h1 class="hero-title">Dr. Martin Corvale<br>Provides Chiropractic<br>Services</h1>

  <section class="mission">
    <p class="mission-script">Getting your body aligned<br>correctly to be a better you</p>
    <p class="mission-text">We use the <span class="hl">latest advancements<br>in chiropractic</span><br>Getting you pain free <span class="hl">is our goal</span></p>
  </section>

  <aside class="services">
    <h2 class="services-title">OUR SERVICES :</h2>
    <ul class="services-list">
      <li>Adjustments</li>
      <li>Xrays</li>
      <li>Wellness exercises</li>
      <li class="note">with a fresh approach<br>to chiropractic</li>
    </ul>
  </aside>

  <div class="offer-strip"></div>
  <div class="offer-band"></div>
  <div class="offer-includes"><span>Consultation</span><span>Exam</span><br><span>Xrays</span></div>
  <div class="offer-price"><div class="lead">First treatment</div><div class="amount">FOR ONLY $50</div></div>

  <svg class="badge" width="250" height="250" viewBox="0 0 250 250" aria-hidden="true">
    <circle cx="125" cy="125" r="123" fill="#8cc63f"/>
    <circle cx="125" cy="125" r="105" fill="#4a4b4d"/>
    <circle cx="125" cy="125" r="94" fill="none" stroke="#ffffff" stroke-width="2.5" stroke-dasharray="6 5"/>
  </svg>
  <div class="badge-text">New<br>Patient<br>Special</div>

  <p class="insurance">WE ALSO ACCEPT MOST INSURANCE PLANS</p>

  <div class="call">
    <span>Call for an appointment</span>
    <span class="call-number">
      <svg width="26" height="26" viewBox="0 0 24 24" aria-hidden="true"><path fill="#8cc63f" d="M6.6 10.8a15.1 15.1 0 0 0 6.6 6.6l2.2-2.2c.3-.3.7-.4 1-.2 1.1.4 2.3.6 3.6.6.6 0 1 .4 1 1V20c0 .6-.4 1-1 1A17 17 0 0 1 3 4c0-.6.4-1 1-1h3.5c.6 0 1 .4 1 1 0 1.3.2 2.5.6 3.6.1.3 0 .7-.2 1z"/></svg>
      618-390-2757
    </span>
  </div>
  <div class="footer-strip"></div>
</main>
</body>
</html>
```